CTWI application splash screen

We need a 1024x768 image for use as an application splash screen.
The image will be displayed full screen on an 10 inch industrial PC 1024x768 screen while our application is launching. The image should convey that the application is "Waiting for connection to Wi-Fi access point..." and include a graphic of the industrial PC connected to the access point via an Ethernet cable. A list of troubleshooting steps should be included at the bottom of the image. The troubleshooting steps should not be the main focus of the image and should be shown in a smaller font (but still readable at 1024x768 displayed on a 10 inch screen).
I will include a mock up of the general idea of what we are looking for as well as image files for the industrial PC, a screenshot of our application to show on the PC's screen and the AP.
For general look and feel and a sense of corporate branding please review our website https://corvanetillageworks.com/. The splash screen should reflect corporate branding.
Target Market(s)
Users of our application
Industry/Entity Type
Agriculture

```html
<!DOCTYPE html>
<html lang="en">
<head>
<meta charset="utf-8">
<title>CTWI – Waiting for Wi-Fi access point</title>
<link rel="stylesheet" href="https://fonts.googleapis.com/css2?family=Questrial&family=Poppins:wght@400;600;700&display=swap">
<style>
  :root {
    --backdrop: #333333;
    --screen-light: #ffffff;
    --screen-grey: #d6d6d6;
    --brand-green: #2bb673;
    --ink: #1f1f1f;
    --ink-soft: #3a3a3a;
    --cable: #1a1a1a;
    --device-dark: #2a2a2a;
    --ap-light: #eeeeee;
  }
  * { margin: 0; padding: 0; box-sizing: border-box; }
  html, body { width: 1200px; height: 1078px; overflow: hidden; }
  body { background: var(--backdrop); font-family: "Poppins", sans-serif; }

  .splash {
    position: absolute; left: 0; top: 89px;
    width: 1200px; height: 900px;
    background: linear-gradient(120deg, var(--screen-light) 0%, #f1f1f1 45%, var(--screen-grey) 100%);
    overflow: hidden;
  }
  .wifi-icon { position: absolute; left: 553px; top: 74px; width: 94px; height: 68px; }
  .status-title {
    position: absolute; left: 0; top: 154px; width: 1200px;
    text-align: center; font-family: "Questrial", sans-serif;
    font-size: 39px; line-height: 50px; color: var(--ink); letter-spacing: 0.5px;
  }
  .cab-computer {
    position: absolute; left: 123px; top: 293px; width: 340px; height: 271px;
    border-radius: 16px;
    background: linear-gradient(180deg, #3a3a3a, var(--device-dark));
  }
  .cab-computer .display {
    position: absolute; left: 33px; top: 25px; width: 276px; height: 207px;
    background: #f4f6f4; border-radius: 2px;
  }
  .access-point {
    position: absolute; left: 1040px; top: 288px; width: 30px; height: 224px;
    border-radius: 8px;
    background: linear-gradient(90deg, #d8d8d8, var(--ap-light), #cfcfcf);
  }
  .cable { position: absolute; left: 0; top: 0; width: 1200px; height: 900px; }
  .diagram-label {
    position: absolute; font-weight: 700; font-size: 19px;
    color: var(--ink-soft); letter-spacing: 0.2px; white-space: nowrap;
  }
  .label-cable { left: 505px; top: 545px; }
  .label-ap { left: 874px; top: 545px; }
  .label-computer { left: 163px; top: 578px; }

  .troubleshooting-tag {
    position: absolute; left: 123px; top: 633px; width: 262px; height: 33px;
    border-radius: 17px; background: var(--brand-green);
    color: #fff; font-weight: 700; font-size: 20px; line-height: 33px; text-align: center;
  }
  .steps, .steps ul { list-style: none; }
  .steps {
    position: absolute; left: 163px; top: 676px;
    font-size: 15px; line-height: 24.5px; color: var(--ink-soft);
  }
  .steps li { position: relative; }
  .steps li::before {
    content: ""; position: absolute; left: -20px; top: 8px;
    width: 10px; height: 10px; border-radius: 50%; background: var(--ink);
  }
  .steps ul { margin-left: 38px; margin-top: 2px; }
  .brand-name {
    position: absolute; left: 990px; top: 790px;
    font-family: "Poppins", sans-serif; font-weight: 700; font-size: 34px;
    color: var(--ink-soft); letter-spacing: 1px;
  }
</style>
</head>
<body>
  <main class="splash">
    <svg class="wifi-icon" viewBox="0 0 94 68" aria-hidden="true">
      <path d="M4 24 A62 62 0 0 1 90 24" fill="none" stroke="var(--brand-green)" stroke-width="11" stroke-linecap="round"/>
      <path d="M22 41 A36 36 0 0 1 72 41" fill="none" stroke="var(--brand-green)" stroke-width="11" stroke-linecap="round"/>
      <path d="M33 54 L47 68 L61 54 A20 20 0 0 0 33 54 Z" fill="var(--brand-green)"/>
    </svg>

    <h1 class="status-title">Waiting for connection to<br>Wi-Fi access point..</h1>

    <svg class="cable" viewBox="0 0 1200 900" aria-hidden="true">
      <path d="M463 527 H1042 Q1054 527 1054 515 V505" fill="none" stroke="var(--cable)" stroke-width="4"/>
      <rect x="458" y="518" width="14" height="18" rx="2" fill="var(--cable)"/>
    </svg>

    <div class="cab-computer" role="img" aria-label="Tractor cab computer showing the seeding application with green row bar chart">
      <div class="display"></div>
    </div>
    <div class="access-point" role="img" aria-label="White outdoor Wi-Fi access point with two antennas and green status light"></div>

    <span class="diagram-label label-cable">ETHERNET CABLE</span>
    <span class="diagram-label label-ap">WI-FI ACCESS POINT</span>
    <span class="diagram-label label-computer">TRACTOR CAB COMPUTER</span>

    <div class="troubleshooting-tag">Troubleshooting steps</div>
    <ul class="steps">
      <li>This screen should only be visible for a short time on boot.</li>
      <li>If this screen stays visible for more than a minute:
        <ul>
          <li>Verify that the Wi-Fi Access Point (AP) powers up when this system does (indicated by a green light on the side of the AP).</li>
          <li>Check the Ethernet cable between this system and the AP for damage, and replace it if necessary.</li>
          <li>Power-cycle this system and wait for it to reboot fully.</li>
          <li>If the issue persists, contact CTWI support for further assistance.</li>
        </ul>
      </li>
    </ul>

    <span class="brand-name">CTWI</span>
  </main>
</body>
</html>
```